High-End Medical Center Website Design Project

This design is part of a well thought-out project by an experienced project manager / developer. The approved wireframe is attached. Creative interpretations / suggestions based on the layout encouraged.

The design is for a new state-of-the-art medical center located in Dallas, Texas. The target audience would likely be individuals (approx. 60% female /40% male) who are the healthcare decision-makers for their families. They would likely have insurance and be inclined to seek out top-quality care.

Potential clients would choose this client over others in their industry because the medical center is physician owned, meaning it is patient-focused rather than profit-focused. The facility is brand new, featuring the latest technology. (This includes an amazing waiting room featuring WiFi and docking stations.) The physicians are hand-picked by referral only.

The look of the site should be extremely clean. We are going for a well-organized, professional look with a bit of a warm glow (interpret that however you like). Use crisp corners and the colors in the logo.

Think modern, clean with some great use of color / font.

We can get lovely photography of the medical center once construction is complete. Feel free to use an "example image" behind the Featured Area ("Physician Owned. Patient-Focused") if you like. We are open to ideas.

ONE CHANGE REQUESTED IN THE WIREFRAME:

Remove the "Connect" 1/4 page footer area and replace with a quick contact form. You may swap the "Locations" area with the form if desired. Put social media icons at the top left of the page in the top header area.

(Note: Please use social media icons that match the design rather than standard icons. We preferred not placing the icons at the top, but the client requested this. Let's not bring more attention to them than necessary.)
Updates

We're custom programming this site, so there's no need to base it on a template. Also, we would prefer not to use typical "seen everywhere" stock images.Thanks.

Industry/Entity Type

Construction

Requirements
Must have
• Follow the wireframe. This has been approved.
Nice to have
• Examples of what hover states, links or dropdowns might look like.

```html
<!DOCTYPE html>
<html lang="en">
<head>
<meta charset="utf-8">
<title>Nova Medical Center</title>
<link rel="stylesheet" href="https://fonts.googleapis.com/css2?family=Amaranth:wght@400;700&display=swap">
<style>
:root{
  --page:#f9f9f9;
  --footer:#f2f2f2;
  --ink:#111111;
  --grey:#8a8a8a;
  --rule:#9a9a9a;
  --nav:#3b3bd6;
  --brand:#1f6fb5;
  --teal:#2aa8b8;
  --hero-top:#3276b8;
  --hero-bottom:#0d3c74;
  --navy:#0f3569;
  --field:#7b7b80;
  --submit:#4b5af2;
  --photo-warm:#d9c7a8;
  --photo-blue:#5f9ad8;
}
*{box-sizing:border-box;margin:0;padding:0}
html,body{width:804px;height:1200px;overflow:hidden}
body{background:var(--page);font-family:"Amaranth",sans-serif;color:var(--ink);position:relative}
.abs{position:absolute}
.nowrap{white-space:nowrap}

.call{left:456px;top:2px;font-size:19px;font-weight:700;color:var(--grey);letter-spacing:1px}
.call strong{color:var(--brand)}
.social{left:705px;top:5px;display:flex;gap:6px}
.social span{width:16px;height:16px;background:#c9c9c9;border:1px solid #aaa;display:block}

.brand{left:23px;top:44px;width:181px;height:27px;display:flex;align-items:center;gap:6px;font-size:14px;font-weight:700;color:var(--brand);letter-spacing:.4px;white-space:nowrap}
.brand i{width:14px;height:14px;background:var(--teal);display:block;flex:none}

.nav{left:268px;top:47px;width:508px;display:flex;justify-content:space-between;font-size:14px;font-weight:700;color:var(--nav);letter-spacing:1.3px;white-space:nowrap}
.nav a{color:inherit;text-decoration:none}

.hero{left:0;top:85px;width:804px;height:360px;background:linear-gradient(180deg,var(--hero-top),var(--hero-bottom))}
.hero-frame{left:19px;top:105px;width:760px;height:303px;background:#fff}
.hero-photo{left:28px;top:108px;width:745px;height:294px;background:linear-gradient(90deg,#ece9e2 0%,var(--photo-warm) 45%,#e4b7a9 75%,#c9c3b8 100%)}
.hero-caption{left:28px;top:244px;width:281px;height:97px;background:#fff;text-align:right;padding:16px 22px 0 0;font-size:26px;line-height:33px;color:#444;letter-spacing:.5px}
.dots{left:368px;top:419px;display:flex;gap:3px}
.dots span{width:9px;height:9px;border-radius:50%;background:#fff;display:block}

.apart-title{left:23px;top:466px;font-size:17px;font-weight:700;letter-spacing:1.5px}
.apart-rule{left:23px;top:500px;width:753px;height:1px;background:var(--rule)}
.apart-pointer{left:98px;top:492px}
.apart-photo{left:24px;top:505px;width:181px;height:68px;background:linear-gradient(90deg,#e8eef4,#b9cde0 50%,#e6edf3)}
.tab{top:504px;font-size:16px;font-weight:700;letter-spacing:1.5px;white-space:nowrap}
.tab-tech{left:239px}
.tab-quality{left:403px}
.tab-patient{left:608px}

.mid-rule{left:23px;top:615px;width:753px;height:1px;background:var(--rule)}
.feature-photo{left:24px;top:636px;width:93px;height:137px;background:linear-gradient(160deg,#9fd0f2,var(--photo-blue) 55%,#2d5f9c)}
.feature-text{left:128px;top:630px;font-size:16px;line-height:28px;font-weight:700;letter-spacing:1.4px;white-space:nowrap}

.testimonial{left:519px;top:636px;width:256px;height:165px;background:#f3f3f3;border:1px solid #9c9c9c;padding:3px 12px}
.testimonial h3{font-size:19px;letter-spacing:2px;font-weight:700;line-height:24px}
.testimonial p{position:absolute;left:17px;top:34px;font-size:10.5px;line-height:18px;font-weight:700;letter-spacing:.5px;white-space:nowrap}
.testimonial p b{font-size:20px;margin-right:3px;line-height:10px}
.read-more{right:8px;bottom:5px;background:var(--navy);color:#fff;font-size:11px;font-weight:700;letter-spacing:1px;padding:1px 7px;border-radius:2px}

.footer{left:0;top:835px;width:804px;height:365px;background:var(--footer)}
.col{top:840px}
.col h4{font-size:23px;font-weight:700;letter-spacing:2.5px;line-height:32px;white-space:nowrap}
.col-news{left:23px}
.col-blog{left:145px}
.col-locations{left:273px}
.col-contact{left:427px}
.col-wait{left:576px;width:215px}
.list{font-size:12px;font-weight:700;line-height:13.5px;letter-spacing:1px;white-space:nowrap}
.list small{display:block;font-size:8.5px;color:var(--grey);line-height:12px;margin-bottom:1px}
.address{font-size:11px;line-height:13.5px;font-weight:700;color:var(--grey);letter-spacing:1px;white-space:nowrap}
.form label{display:block;font-size:13px;font-weight:700;letter-spacing:1px;color:#333}
.field{width:128px;height:27px;background:var(--field);border-radius:2px}
.field-tall{height:52px}
.submit{display:inline-block;margin-top:12px;background:var(--submit);color:#fff;font-size:12px;font-weight:700;letter-spacing:1.2px;padding:2px 10px;border-radius:2px}
.wait-title{font-size:19px !important;letter-spacing:2.3px !important}
.wait-time{font-size:12px;font-weight:700;letter-spacing:1px;margin:2px 0 6px}
.wait-copy{font-size:7.5px;line-height:10.5px;font-weight:700;letter-spacing:.3px;white-space:nowrap}

.copyright{left:21px;top:1178px;font-size:11px;font-weight:700;letter-spacing:1px}
.footer-links{right:6px;top:1180px;font-size:8px;font-weight:700}
</style>
</head>
<body>

<div class="abs call">Call Us: <strong>(555) 010-2040</strong></div>
<div class="abs social" aria-label="Social links"><span></span><span></span><span></span></div>

<div class="abs brand"><i></i>NOVA MEDICAL CENTER</div>
<nav class="abs nav">
  <a href="#">Why Nova</a><a href="#">Physician</a><a href="#">Specialist</a><a href="#">Info</a><a href="#">Location</a><a href="#">Contact</a>
</nav>

<section class="abs hero"></section>
<div class="abs hero-frame"></div>
<div class="abs hero-photo" role="img" aria-label="Nurse in pink scrubs caring for a smiling senior patient in a bright room"></div>
<div class="abs hero-caption">We care about<br>every patient</div>
<div class="abs dots"><span></span><span></span><span></span></div>

<h2 class="abs apart-title">What Safe us Apart</h2>
<div class="abs apart-rule"></div>
<svg class="abs apart-pointer" width="12" height="8" viewBox="0 0 12 8"><path d="M0 8 L6 0 L12 8 Z" fill="#888"/></svg>
<div class="abs apart-photo" role="img" aria-label="Team of physicians in white coats"></div>
<div class="abs tab tab-tech">Technology</div>
<div class="abs tab tab-quality">Quality Of Core</div>
<div class="abs tab tab-patient">Patient Experience</div>

<div class="abs mid-rule"></div>
<div class="abs feature-photo" role="img" aria-label="Surgical team in blue gowns under operating lights"></div>
<p class="abs feature-text">Lorem ipsum dolor sit amet, consecte-<br>tur adipiscing elit. Cras ac felis.<br>Donec aliquet posuere vulputate. Ali-<br>quam malesuada tortor quis magna<br>pretium sit amet rhoncus risus pre-</p>

<aside class="abs testimonial">
  <h3>Testimonials</h3>
  <p><b>&ldquo;</b>Sed ut perspiciatis unde omnis iste<br>natus error sit voluptatem accusan-<br>tium doloreue laudantium, totam rem<br>aperiam, eaque ipsa quae ab illo<br>Lorem ipsum dolor sit amet, consecte-</p>
  <span class="abs read-more">Read More</span>
</aside>

<footer class="abs footer"></footer>
<div class="abs col col-news">
  <h4>News</h4>
  <div class="list">Title Text here<br>Title Text here<br>Title Text here</div>
</div>
<div class="abs col col-blog">
  <h4>Blog</h4>
  <div class="list">Title Text here<small>January 1,2013</small>Title Text here<small>January 1,2013</small>Title Text here<small>January 1,2013</small></div>
</div>
<div class="abs col col-locations">
  <h4>Locations</h4>
  <div class="address">111 Name of the St.<br>Dallas,Texas<br>ZIP code</div>
</div>
<div class="abs col col-contact form">
  <h4>Contact</h4>
  <label>Name</label><div class="field"></div>
  <label style="margin-top:12px">Email</label><div class="field"></div>
  <label style="margin-top:14px">Message</label><div class="field field-tall"></div>
  <span class="submit">Submit</span>
</div>
<div class="abs col col-wait">
  <h4 class="wait-title">Average Wait Time</h4>
  <div class="wait-time">9 Minutes</div>
  <p class="wait-copy">Lorem ipsum dolor sit amet, consectetur<br>adipiscing elit. Cras ac felis. Donec aliquet<br>posuere vulputate. Aliquam malesuada tortor<br>quis magna pretium sit amet rhoncus risus<br>pretium. Phasellus interdum bibendum purus,<br>ac venenatis orci egestas.</p>
</div>

<div class="abs copyright">&copy; 2012 Nova Medical Center</div>
<div class="abs footer-links">Home / Sitemap / RSS / Back to Top</div>

</body>
</html>
```